Business Card - Rebranding for Consulting Firm

We are renaming and rebranding our consulting firm and need to raise the level of quality of our cards as part of that effort. We consult to leading high tech, life science and other innovation sector companies.

Need a two-sided business card design.

Side 1: (a) Company logo (b) tag line: Optimize Your Investment in Talent (c) Name (d) Title (e) Phone 1: Office (f) Phone 2: Mobile (g) email: person@HollowmereAdvisory.com

Side 2: Two lines of text: (a) Growth is Imperative. Change is Constant. Talent Executes Strategy. (b) We help you excel at all three.

Target Market(s)

Business and human resources executives and senior managers

Industry/Entity Type

Management Consulting

Contact Information for Business Card

Font styles to use
Sans Serif

Requirements
Must have
• clean, not too busy, but with a bit of creativity. Stick to the colors used in the attached logo
• appeal to high tech, life science companies
Nice to have
• prefer white background

```html
<!DOCTYPE html>
<html lang="en">
<head>
<meta charset="utf-8">
<title>Hollowmere Advisory – Business Card</title>
<link rel="stylesheet" href="https://fonts.googleapis.com/css2?family=Source+Sans+3:wght@300;400;600;700&display=swap">
<style>
  :root {
    --page-bg: #e9ebee;
    --card-white: #ffffff;
    --brand-blue: #0b5a9c;
    --brand-blue-light: #0a72b6;
    --brand-blue-deep: #08528f;
    --text-grey: #8a8d91;
    --tagline-grey: #4d6a85;
    --on-blue: #ffffff;
  }
  * { box-sizing: border-box; margin: 0; padding: 0; }
  html, body {
    width: 1200px; height: 1200px; overflow: hidden;
    background: var(--page-bg);
    font-family: "Source Sans 3", "Myriad Pro", sans-serif;
  }
  .canvas {
    width: 1200px; height: 1200px;
    display: flex; flex-direction: column; align-items: center; justify-content: center;
    gap: 60px;
  }
  .card {
    width: 900px; height: 514px; position: relative;
    box-shadow: 0 10px 30px rgba(0,0,0,0.15);
  }
  /* Front */
  .card--front { background: var(--card-white); }
  .brand {
    position: absolute; top: 70px; right: 90px;
    display: flex; align-items: center; gap: 18px;
  }
  .brand__mark { width: 44px; height: 44px; background: var(--brand-blue-light); }
  .brand__name {
    font-size: 56px; font-weight: 400; color: var(--brand-blue); letter-spacing: -0.5px;
  }
  .person { position: absolute; top: 220px; left: 110px; }
  .person__line { display: flex; align-items: baseline; gap: 14px; }
  .person__name { font-size: 30px; font-weight: 700; color: var(--brand-blue); }
  .person__title { font-size: 26px; font-weight: 300; color: var(--text-grey); }
  .contact { margin-top: 18px; margin-left: 30px; list-style: none; }
  .contact li { font-size: 26px; font-weight: 300; color: var(--text-grey); line-height: 1.32; }
  .tagline {
    position: absolute; right: 90px; bottom: 70px;
    font-size: 24px; font-weight: 600; color: var(--tagline-grey);
  }
  /* Back */
  .card--back {
    background: linear-gradient(180deg, var(--brand-blue-light) 0%, var(--brand-blue-deep) 100%);
    color: var(--on-blue);
  }
  .manifesto { position: absolute; top: 110px; left: 110px; }
  .manifesto__lines { list-style: none; }
  .manifesto__lines li { font-size: 32px; font-weight: 300; line-height: 1.25; }
  .manifesto__lines li:nth-child(2) { margin-left: 24px; }
  .manifesto__lines li:nth-child(3) { margin-left: 48px; }
  .manifesto__promise { margin-top: 34px; margin-left: 72px; font-size: 34px; font-weight: 700; }
  .website {
    position: absolute; left: 210px; bottom: 80px;
    font-size: 26px; font-weight: 300;
  }
</style>
</head>
<body>
<main class="canvas">
  <section class="card card--front" aria-label="Card front">
    <div class="brand">
      <span class="brand__mark" aria-hidden="true"></span>
      <span class="brand__name">Hollowmere Advisory</span>
    </div>
    <div class="person">
      <p class="person__line">
        <span class="person__name">Yourfirst Andlastname</span>
        <span class="person__title">- Title of the Individual</span>
      </p>
      <ul class="contact">
        <li>(123) 456-7890 mobile</li>
        <li>(123) 123-4567 office</li>
        <li>person@HollowmereAdvisory.com</li>
      </ul>
    </div>
    <p class="tagline">Optimize Your Investment in Talent</p>
  </section>

  <section class="card card--back" aria-label="Card back">
    <div class="manifesto">
      <ul class="manifesto__lines">
        <li>Growth is Imperative.</li>
        <li>Change is Constant.</li>
        <li>Talent Executes Strategy.</li>
      </ul>
      <p class="manifesto__promise">We help you excel at all three.</p>
    </div>
    <p class="website">www.HollowmereAdvisory.com</p>
  </section>
</main>
</body>
</html>
```